Looking for awesome business card design with attached existing logo

We are a water, mold, and fire damage restoration company called "Falcon Shield" Looking for an awesome business card that is edgy yet professional and unique. Show me what you got!

```html
<!DOCTYPE html>
<html lang="en">
<head>
<meta charset="utf-8">
<title>Falcon Shield – Business Card</title>
<link rel="stylesheet" href="https://fonts.googleapis.com/css2?family=Open+Sans:wght@400;600;700&display=swap">
<style>
  :root {
    --stage: #9a9a9a;
    --card: #1f1f23;
    --card-edge: #16161a;
    --gold: #e3a12b;
    --slate: #3d5f70;
    --ink-light: #f2f2f2;
    --emboss-1: #2a2a2f;
    --emboss-2: #121215;
  }
  * { box-sizing: border-box; margin: 0; padding: 0; }
  html, body { width: 1200px; height: 876px; overflow: hidden; }
  body {
    background: var(--stage);
    font-family: "Open Sans", Arial, sans-serif;
    display: flex;
    align-items: center;
    justify-content: center;
    gap: 60px;
  }
  .card {
    position: relative;
    width: 520px;
    height: 300px;
    background: var(--card);
    border-radius: 3px;
    box-shadow: 0 10px 24px rgba(0,0,0,.35);
    overflow: hidden;
  }

  /* Front */
  .brand {
    position: absolute;
    top: 34px; left: 34px;
    display: flex; align-items: center; gap: 10px;
  }
  .brand-dot {
    width: 22px; height: 22px; border-radius: 50%;
    background: var(--gold);
  }
  .brand-name {
    font-weight: 700; font-size: 28px; color: var(--gold);
    letter-spacing: .5px;
  }
  .contact {
    position: absolute; top: 96px; left: 34px;
    list-style: none;
    color: var(--ink-light); font-size: 12.5px; line-height: 1.55;
  }
  .contact li { display: flex; align-items: center; gap: 8px; }
  .contact .address { padding-left: 20px; }
  .contact svg { width: 12px; height: 12px; fill: var(--gold); flex: none; }
  .emblem-area {
    position: absolute; left: 34px; bottom: 0;
    width: 210px; height: 110px;
    border-radius: 110px 110px 0 0;
    background: radial-gradient(circle at 50% 80%, var(--emboss-1), var(--emboss-2));
  }
  .person {
    position: absolute; right: 46px; bottom: 44px;
    text-align: right;
  }
  .person-name { font-weight: 700; font-size: 24px; }
  .person-name .first { color: var(--gold); }
  .person-name .last { color: var(--slate); }
  .person-role { color: var(--ink-light); font-size: 14px; margin-top: 2px; }
  .gold-tab {
    position: absolute; right: 0; bottom: 44px;
    width: 26px; height: 34px; background: var(--gold);
  }

  /* Back */
  .pattern-area {
    position: absolute; inset: 0;
    background: linear-gradient(120deg, #1c1c20 0%, #1f1f23 55%, #3a3a40 85%, #5a5a60 100%);
  }
  .back-brand {
    position: absolute; left: 50%; top: 60%;
    transform: translate(-50%, -50%);
    display: flex; align-items: center; gap: 8px;
  }
  .back-brand .brand-dot { width: 16px; height: 16px; }
  .back-brand .brand-name { font-size: 22px; }
</style>
</head>
<body>

<section class="card card-front">
  <div class="brand">
    <span class="brand-dot"></span>
    <span class="brand-name">Falcon Shield</span>
  </div>

  <ul class="contact">
    <li class="address">418 Harbor Ridge Rd. Suite 120</li>
    <li class="address">Lakeside, TX 75010</li>
    <li>
      <svg viewBox="0 0 24 24"><path d="M6.6 10.8a15.1 15.1 0 0 0 6.6 6.6l2.2-2.2a1 1 0 0 1 1-.25 11.4 11.4 0 0 0 3.6.57 1 1 0 0 1 1 1V20a1 1 0 0 1-1 1A17 17 0 0 1 3 4a1 1 0 0 1 1-1h3.5a1 1 0 0 1 1 1c0 1.25.2 2.45.57 3.57a1 1 0 0 1-.25 1z"/></svg>
      (555) 204-1187
    </li>
    <li>
      <svg viewBox="0 0 24 24"><path d="M2 5h20v14H2z M2 5l10 8 10-8" fill="none" stroke="#e3a12b" stroke-width="2.4"/></svg>
      info@falconshield.example
    </li>
    <li>
      <svg viewBox="0 0 24 24"><circle cx="12" cy="12" r="9" fill="none" stroke="#e3a12b" stroke-width="2.4"/><path d="M3 12h18M12 3c3 3 3 15 0 18M12 3c-3 3-3 15 0 18" fill="none" stroke="#e3a12b" stroke-width="2"/></svg>
      www.falconshield.example
    </li>
  </ul>

  <div class="emblem-area" role="img" aria-label="Large embossed brand emblem decoration"></div>

  <div class="person">
    <div class="person-name"><span class="first">Lena</span> <span class="last">Marsh</span></div>
    <div class="person-role">Managing Director</div>
  </div>
  <div class="gold-tab"></div>
</section>

<section class="card card-back">
  <div class="pattern-area" role="img" aria-label="Repeating pattern of the brand emblem with a glossy highlight"></div>
  <div class="back-brand">
    <span class="brand-dot"></span>
    <span class="brand-name">Falcon Shield</span>
  </div>
</section>

</body>
</html>
```